GKL Auto - help to get me noticed

We not long ago tasked Pixel Harbor to design a logo for my business. I'm happy with the result so would like to have a business card designed as a follow up.

It's an Automotive service and repair business that offers the following -
- Servicing
- General repairs
- Brakes
- Detailing
- Integrity

GKL Automotive
Malcolm Pryde
0491 726 183

Target Market(s)

Everyday people with the ability to reach out to corporate customers also.

Industry/Entity Type

Automotive

Contact Information for Business Card

Black card, logo, name and phone number on front. Other details on back of card.

```html
<!DOCTYPE html>
<html lang="en">
<head>
<meta charset="utf-8">
<title>GKL Automotive – Business Card</title>
<link rel="stylesheet" href="https://fonts.googleapis.com/css2?family=Chakra+Petch:ital,wght@1,700&family=Lato:wght@400;900&display=swap">
<style>
  :root {
    --stage: #262628;
    --card: #131315;
    --lime: #b3d235;
    --green: #8cc63f;
    --white: #ffffff;
    --text-soft: #e9e9e9;
  }
  * { margin: 0; padding: 0; box-sizing: border-box; }
  html, body { width: 1200px; height: 900px; overflow: hidden; }
  body {
    background: var(--stage);
    display: flex;
    flex-direction: column;
    align-items: center;
    justify-content: center;
    gap: 36px;
    font-family: "Lato", sans-serif;
  }
  .card {
    position: relative;
    width: 700px;
    height: 400px;
    background: var(--card);
    border-radius: 4px;
    box-shadow: 0 14px 30px rgba(0,0,0,0.45);
    overflow: hidden;
  }

  /* Wordmark */
  .wordmark {
    position: absolute;
    display: flex;
    align-items: center;
    gap: 14px;
    font-family: "Lato", sans-serif;
    font-weight: 900;
    color: var(--green);
    text-transform: uppercase;
    letter-spacing: 2px;
    line-height: 1;
  }
  .wordmark__square {
    width: 30px;
    height: 30px;
    background: var(--green);
  }

  /* Front */
  .card--front .holder {
    position: absolute;
    left: 70px;
    top: 78px;
  }
  .holder__name {
    font-family: "Chakra Petch", sans-serif;
    font-style: italic;
    font-weight: 700;
    font-size: 44px;
    letter-spacing: 2px;
    color: var(--green);
    text-transform: uppercase;
    line-height: 1;
  }
  .holder__rule {
    width: 180px;
    height: 1px;
    background: var(--green);
    margin: 14px 0 12px;
  }
  .holder__phone {
    display: flex;
    align-items: center;
    gap: 10px;
    font-family: "Chakra Petch", sans-serif;
    font-style: italic;
    font-weight: 700;
    font-size: 26px;
    letter-spacing: 1px;
    color: var(--white);
  }
  .holder__phone svg { width: 22px; height: 22px; }
  .card--front .wordmark {
    right: 70px;
    bottom: 80px;
    font-size: 38px;
  }

  /* Back */
  .card--back .wordmark {
    right: 90px;
    top: 70px;
    font-size: 46px;
  }
  .services {
    position: absolute;
    left: 60px;
    right: 50px;
    top: 220px;
    color: var(--text-soft);
  }
  .services__intro {
    font-size: 21px;
    font-weight: 400;
    margin-bottom: 16px;
  }
  .services__list {
    list-style: none;
    display: flex;
    gap: 30px;
    font-size: 21px;
  }
  .services__list li {
    display: flex;
    align-items: center;
    gap: 9px;
  }
  .services__list li::before {
    content: "";
    width: 6px;
    height: 6px;
    border-radius: 50%;
    background: var(--green);
  }
</style>
</head>
<body>
  <section class="card card--front" aria-label="Business card front">
    <div class="holder">
      <p class="holder__name">Malcolm Pryde</p>
      <div class="holder__rule"></div>
      <p class="holder__phone">
        <svg viewBox="0 0 24 24" aria-hidden="true">
          <path fill="var(--green)" d="M6.6 10.8c1.4 2.8 3.8 5.1 6.6 6.6l2.2-2.2c.3-.3.7-.4 1-.2 1.1.4 2.3.6 3.6.6.6 0 1 .4 1 1V20c0 .6-.4 1-1 1C10.6 21 3 13.4 3 4c0-.6.4-1 1-1h3.5c.6 0 1 .4 1 1 0 1.3.2 2.5.6 3.6.1.3 0 .7-.2 1z"/>
        </svg>
        0491 726 183
      </p>
    </div>
    <div class="wordmark"><span class="wordmark__square"></span>GKL Automotive</div>
  </section>

  <section class="card card--back" aria-label="Business card back">
    <div class="wordmark"><span class="wordmark__square"></span>GKL Automotive</div>
    <div class="services">
      <p class="services__intro">It's an Automotive service and repair business that offers the following</p>
      <ul class="services__list">
        <li>Servicing</li>
        <li>General repairs</li>
        <li>Brakes</li>
        <li>Detailing</li>
        <li>Integrity</li>
      </ul>
    </div>
  </section>
</body>
</html>
```